Valtimore Sciences needs high end Label Design for a revolutionary new supplement

We at Valtimore Sciences are looking for a brand new Label Design for a first of its kind product called Tolmisse. It is the first supplement on the market that treats grief and heartbreak. This product is unisex for both men and woman. We want the New Label to look high end and luxurious using the brand colors which are gold and burgundy. Please feel free to use other colors such as black, white, or gray to go along with it or any other colors if you feel would be a great fit! Valtimore Sciences is like the Quorvel of the supplement world, coming out with new products that will challenge the way people treat different symptoms. To Recap:

1. Product Name: TOLMISSE - the font will play a big roll
2. The Label will be placed on an all white bottle
3. Some parts of the label will be printed with foil to make parts of the label shiny and more attractive. Please keep this in mind when designing.
4. Must use our Logo. I will attach a file of our logo and of the emblem as well. Feel free to use the emblem separately if you have a great idea for it. Please let us know if you need the Logo in a different file type.
5. This all natural herbal supplement in pill form is the first to treat grief and support someone with a broken heart. The consumers purchasing this product will be going through a hard and emotional time. This is a serious product.
6. The manufacturer has included some basic instructions regarding the dye line and file types. Please do your best to meet these. If you cannot meet the guidelines please submit art work anyways. If your design is chosen we will just have the manufacturer replicate the design.

The final label should portray Tolmisse and Valtimore Sciences as a luxurious brand and product which was made with cutting edge science leading the way with revolutionary ideas. We want customers to feel that the product is worth every penny, because it is. As soon as they receive the product and take one look at the label, I want them to think WOW I made the right choice buying this. I have attached some Label designs that we really liked for your review.

Please feel free to message me with any questions or if you need the Logo in a different file type. Thank you all.
Updates

Please send in more entries while we take a couple days to review, we are still looking for that one design we can work with. We are getting close, thank you all!

Target Market(s)

People going through grief and heartbreak.

Font styles to use
Sans Serif
Script
Other font styles liked:
• Any font that looks good, The font for the name TOLMISSE is very important and will brand it. We hated the font used in the label we received in our first label draft (attached so you can see)

Requirements
Must have
• Must have the company Logo that says the company name
• Must have the colors Gold and Burgundy
• Must have some areas that will be the shiny foil when label is printed.
• Must say "Dietary Supplement" somewhere near the bottom along with "90 Capsules"
• I have attached a Label someone designed for us but were not really happy with. I did like the font the "Dietary supplement" and "90 Capsules" had and also where it was placed. We absolutely HATED the font used for Tolmisse.
• Must look at the label design we received from the manufacturer and take into consideration the room needed to write in the directions and all the symbols such as "made in america" and "Valtimore Sciences Facility" Don't worry about adding these in as they will put those in before printing but keep in mind they will be added to the Final Label along with the Supplement Facts.
Nice to have
• Would like to see other colors to go with gold and burgundy suck as black, white, or gray. I have attached some Label designs that I really liked for your reference.
Should not have
• Does not need to have any other legal language, that will be applied by the the manufacturer's graphics team.

```html
<!DOCTYPE html>
<html lang="en">
<head>
<meta charset="utf-8">
<title>Tolmisse Label</title>
<link rel="stylesheet" href="https://fonts.googleapis.com/css2?family=Montserrat:wght@400;500;700&family=Space+Mono&display=swap">
<style>
  :root {
    --burgundy: #7d0101;
    --gold-light: #dcae6c;
    --gold-mid: #cf9a4c;
    --gold-deep: #bf8428;
    --white: #ffffff;
    --ink: #2a1a0a;
  }
  * { margin: 0; padding: 0; box-sizing: border-box; }
  html, body {
    width: 1200px;
    height: 462px;
    overflow: hidden;
    background: var(--burgundy);
  }
  .label {
    position: relative;
    width: 1200px;
    height: 462px;
    background: var(--burgundy);
    font-family: "Montserrat", sans-serif;
  }
  .foil-stroke {
    position: absolute;
    left: 386px;
    top: 108px;
    width: 428px;
    height: 250px;
  }
  .product-name {
    position: absolute;
    left: 0;
    width: 1200px;
    top: 163px;
    text-align: center;
    font-family: "Space Mono", monospace;
    font-weight: 400;
    font-size: 86px;
    line-height: 86px;
    letter-spacing: 2px;
    color: transparent;
    -webkit-text-stroke: 1.2px var(--white);
  }
  .rule {
    position: absolute;
    left: 497px;
    width: 209px;
    height: 2px;
    background: var(--white);
  }
  .rule--top { top: 264px; }
  .rule--bottom { top: 290px; }
  .product-type {
    position: absolute;
    left: 0;
    width: 1200px;
    top: 271px;
    text-align: center;
    font-size: 11px;
    line-height: 16px;
    font-weight: 500;
    letter-spacing: 0.6px;
    color: var(--ink);
  }
  .product-count {
    position: absolute;
    left: 0;
    width: 1200px;
    top: 302px;
    text-align: center;
    color: var(--white);
    line-height: 28px;
  }
  .product-count__number {
    font-size: 21px;
    font-weight: 700;
    letter-spacing: 1px;
    vertical-align: middle;
  }
  .product-count__unit {
    font-size: 10px;
    font-weight: 500;
    letter-spacing: 0.5px;
    margin-left: 5px;
    vertical-align: middle;
  }
  .company-mark {
    position: absolute;
    left: 958px;
    top: 116px;
    display: flex;
    align-items: center;
    gap: 10px;
    color: var(--white);
  }
  .company-mark__seal {
    width: 46px;
    height: 46px;
    border: 2px solid var(--white);
    border-radius: 50%;
    flex: none;
  }
  .company-mark__name {
    font-size: 19px;
    font-weight: 700;
    line-height: 22px;
    letter-spacing: 1px;
    text-transform: uppercase;
  }
</style>
</head>
<body>
  <div class="label">
    <svg class="foil-stroke" viewBox="0 0 428 250" role="img" aria-label="Gold foil brush stroke behind the product name">
      <defs>
        <linearGradient id="foilGold" x1="0" y1="0" x2="1" y2="0.25">
          <stop offset="0" stop-color="#dcae6c"/>
          <stop offset="0.5" stop-color="#cf9a4c"/>
          <stop offset="1" stop-color="#bf8428"/>
        </linearGradient>
      </defs>
      <path fill="url(#foilGold)" d="M60 20 C140 -4 250 0 320 30 C380 60 420 150 426 205 C428 232 400 246 360 240 C290 232 200 250 130 236 C70 226 10 220 4 180 C-2 140 10 90 30 55 C38 38 46 26 60 20 Z"/>
    </svg>

    <h1 class="product-name">TOLMISSE</h1>
    <div class="rule rule--top"></div>
    <p class="product-type">DIETARY SUPPLEMENT</p>
    <div class="rule rule--bottom"></div>
    <p class="product-count">
      <span class="product-count__number">90</span><span class="product-count__unit">CAPSULES</span>
    </p>

    <div class="company-mark">
      <span class="company-mark__seal"></span>
      <span class="company-mark__name">Valtimore<br>Sciences</span>
    </div>
  </div>
</body>
</html>
```